Zanquerra Business Card Design

Zanquerra is a small and new restaurant/ bar location in Hong Kong. The name "Djibouti" derives from an African country. There is no specific reason behind other than the fact, that the bar is somewhat inspired by African elements (only inspired but not purely based on African cuisine etc.).

The bar is somewhat a fusion of African, Mediterranean and Oriental (Old French Vietnam) elements.

However, it is very imperative to stress, that the overall look and feel of Zanquerra is a very high end cocktail lounge/ bar location. The bar is tucked away in a hidden alley, so people will have to know about it. The idea is to send the consumer off in an Escape or hidden remote location where they are at ease in a hip, stylish and trendy environment.

The card needs to feel high-end.

Final logo artwork has been attached and also pictures of the bar/ restaurant itself. The logo ie monkey head cannot be modified. However, the background color and the color of the type "ZANQUERRA" can be changed.

The following details need to fit onto the business card. Of course they can be arranged to your liking:

LOGO

Tobin Le
Partner

+852 90817364
xxx@zanquerra-bar.com
www.zanquerra-bar.com
4C, Pelham Lane, Wan Chai, Hong Kong

Industry/Entity Type

Restaurant

```html
<!DOCTYPE html>
<html lang="en">
<head>
<meta charset="UTF-8">
<title>Zanquerra Business Card</title>
<link href="https://fonts.googleapis.com/css2?family=Questrial&display=swap" rel="stylesheet">
<style>
  :root {
    --backdrop: #e8e3da;
    --card: #ffffff;
    --ink: #231f1c;
    --ink-soft: #3a3430;
    --gold: #8a6a3a;
    --mark-dark: #1f1a16;
    --mark-mid: #3b2f25;
    --shadow: rgba(40, 28, 18, 0.25);
  }
  * { margin: 0; padding: 0; box-sizing: border-box; }
  html, body {
    width: 1200px;
    height: 1023px;
    overflow: hidden;
    background: var(--backdrop);
    font-family: "Questrial", "Century Gothic", sans-serif;
    color: var(--ink);
  }
  .stage {
    width: 1200px;
    height: 1023px;
    display: flex;
    justify-content: center;
    align-items: center;
    gap: 80px;
  }
  .card {
    width: 380px;
    height: 620px;
    background: var(--card);
    box-shadow: 0 10px 30px var(--shadow);
    display: flex;
    flex-direction: column;
    align-items: center;
  }
  .logo-mark {
    border-radius: 50%;
    border: solid var(--ink);
    background: radial-gradient(circle at 50% 55%, var(--mark-mid) 0%, var(--mark-dark) 70%);
    box-shadow: inset 0 0 0 8px var(--card);
  }
  /* Front */
  .card--front { justify-content: center; }
  .front-mark {
    width: 350px;
    height: 350px;
    border-width: 6px;
    box-shadow: inset 0 0 0 12px var(--card);
  }
  /* Back */
  .card--back { padding-top: 56px; text-align: center; }
  .back-mark {
    width: 196px;
    height: 196px;
    border-width: 4px;
  }
  .brand-name {
    margin-top: 26px;
    font-size: 46px;
    font-weight: 400;
    letter-spacing: 2px;
    color: var(--ink);
    line-height: 1;
  }
  .person-name {
    margin-top: 22px;
    font-size: 27px;
    color: var(--ink);
  }
  .person-role {
    font-size: 16px;
    color: var(--gold);
    margin-top: 2px;
  }
  .contact-list {
    list-style: none;
    margin-top: 32px;
    font-size: 17px;
    line-height: 1.45;
  }
  .contact-list .label { color: var(--ink-soft); }
  .contact-list .value { color: var(--gold); }
  .address {
    margin-top: 22px;
    font-size: 17px;
    line-height: 1.35;
    color: var(--gold);
  }
</style>
</head>
<body>
  <main class="stage">
    <section class="card card--front" aria-label="Card front">
      <div class="logo-mark front-mark" role="img" aria-label="Zanquerra logo mark, illustrated emblem in a ring"></div>
    </section>

    <section class="card card--back" aria-label="Card back">
      <div class="logo-mark back-mark" role="img" aria-label="Zanquerra logo mark, illustrated emblem in a ring"></div>
      <h1 class="brand-name">ZANQUERRA</h1>
      <p class="person-name">Tobin Le</p>
      <p class="person-role">Partner</p>
      <ul class="contact-list">
        <li><span class="label">[P]</span> <span class="value">+852 90817364</span></li>
        <li><span class="label">[E]</span> <span class="value">tobinle@zanquerra-bar.com</span></li>
        <li><span class="label">[W]</span> <span class="value">www.zanquerra-bar.com</span></li>
      </ul>
      <p class="address">4C, Pelham Lane, Wan Chai,<br>Hong Kong</p>
    </section>
  </main>
</body>
</html>
```